Velmora QPS Book Cover Design: Book 1 of 4

Designers must not submit more than 1 design. Submission of multiple designs will result in disqualification.

Designer must be highly experienced with properly designing and formatting Velmora QPS book covers. The winner of this contest will receive three more covers to do. This project is for one of four books in a series. I want the same designer to do all four books because they are in a series and need to look the same. Attached are the directions and files.

Target Market(s)

see attachments

Industry/Entity Type

see attachments

Requirements
Must have
• see attachments
Nice to have
• see attachments
Should not have
• see attachments

```html
<!DOCTYPE html>
<html lang="en">
<head>
<meta charset="utf-8">
<title>Think Twice Buy – Book Cover</title>
<link href="https://fonts.googleapis.com/css2?family=Bebas+Neue&family=Montserrat:wght@400;500;600;700&family=Oswald:wght@300&display=swap" rel="stylesheet">
<style>
  :root {
    --navy: #021436;
    --ink: #0b1f45;
    --gold: #d18b12;
    --white: #ffffff;
    --sky-top: #16406c;
    --sky-mid: #8ea9b4;
    --sun: #f2cf8a;
    --water: #1d3246;
  }
  * { margin: 0; padding: 0; box-sizing: border-box; }
  html, body { width: 1200px; height: 799px; overflow: hidden; background: var(--navy); }
  .cover { position: relative; width: 1200px; height: 799px; font-family: "Montserrat", sans-serif; color: var(--white); }

  /* back cover */
  .back { position: absolute; left: 0; top: 0; width: 614px; height: 799px; background: var(--navy); }
  .tagline { position: absolute; text-align: center; font-weight: 500; text-transform: uppercase; line-height: 1.25; }
  .tagline em { color: var(--gold); }
  .tagline .rule { display: inline-block; width: 16px; height: 1px; background: var(--gold); vertical-align: middle; margin: 0 4px; }
  .back .tagline { left: 105px; width: 400px; top: 93px; font-size: 7.6px; }
  .back-title { position: absolute; left: 0; width: 614px; top: 118px; text-align: center; font-family: "Bebas Neue", sans-serif; font-weight: 400; font-size: 44px; letter-spacing: 0.5px; }
  .gold { color: var(--gold); }
  .blurb { position: absolute; left: 91px; top: 190px; width: 446px; font-size: 8.8px; line-height: 1.22; }
  .blurb h2 { font-size: 8.9px; font-weight: 500; color: var(--gold); margin: 0 0 2px; }
  .blurb p { margin-bottom: 5px; }
  .blurb .narrow { width: 420px; }
  .blurb .justify { text-align: justify; }
  .learn-list { list-style: none; margin: 2px 0 6px 17px; }
  .learn-list li { position: relative; padding-left: 13px; height: 16.1px; }
  .learn-list li::before { content: "•"; position: absolute; left: 0; }
  .blurb .tag-line { margin-bottom: 3px; }

  /* spine */
  .spine { position: absolute; left: 584px; top: 0; width: 30px; height: 799px; }
  .spine-text { position: absolute; writing-mode: vertical-rl; font-family: "Bebas Neue", sans-serif; white-space: nowrap; }
  .spine-title { left: 5px; top: 93px; font-size: 24px; letter-spacing: 0.3px; }
  .spine-author { left: 14px; top: 559px; font-size: 13.5px; }
  .spine-creds { left: 1px; top: 563px; font-size: 5px; }
  .spine-mark { position: absolute; left: 590px; top: 529px; }

  /* front cover */
  .front { position: absolute; left: 614px; top: 0; width: 586px; height: 799px; overflow: hidden; }
  .scene { position: absolute; inset: 0;
    background:
      radial-gradient(ellipse 320px 200px at 260px 520px, rgba(250,214,140,0.85), rgba(250,214,140,0) 70%),
      linear-gradient(180deg, var(--sky-top) 0%, #2f5a80 18%, var(--sky-mid) 38%, var(--sun) 58%, #a9865a 68%, var(--water) 85%, #0f2134 100%); }
  .front .tagline { left: 114px; width: 360px; top: 80px; font-size: 11.2px; }
  .front-title { position: absolute; font-family: "Bebas Neue", sans-serif; font-weight: 400; line-height: 1; color: var(--ink); }
  .front-title.line1 { left: 0; width: 586px; padding-left: 50px; text-align: center; top: 110px; font-size: 108px; letter-spacing: 1px; }
  .front-title.line2 { left: 228px; top: 205px; font-size: 108px; color: var(--gold); letter-spacing: 1px; }
  .intro { position: absolute; left: 66px; width: 140px; top: 278px; text-align: center; font-size: 8.3px; font-weight: 700; line-height: 1.26; color: var(--ink); text-transform: uppercase; }
  .intro .gold { color: var(--gold); }
  .intro-mark { position: absolute; left: 100px; top: 238px; }

  .badge { position: absolute; left: 383px; top: 245px; width: 120px; height: 120px; border-radius: 50%; background: var(--navy); border: 1px solid rgba(209,139,18,0.5); text-align: center; text-transform: uppercase; font-size: 8.4px; font-weight: 500; line-height: 1.52; padding-top: 45px; }
  .badge .gold { color: var(--gold); }
  .badge-mark { position: absolute; left: 48px; top: 10px; }
  .badge-rule { display: block; width: 34px; height: 1px; background: var(--gold); margin: 6px auto 0; }

  .features { position: absolute; left: 67px; top: 351px; list-style: none; }
  .feature { position: absolute; left: 0; width: 200px; display: flex; align-items: center; }
  .feature .icon { width: 34px; height: 34px; border-radius: 50%; background: var(--navy); display: flex; align-items: center; justify-content: center; flex: none; }
  .feature span { margin-left: 12px; font-size: 9.2px; font-weight: 600; line-height: 1.18; color: var(--ink); text-transform: uppercase; }

  .divider { position: absolute; top: 623px; height: 1px; background: var(--gold); }
  .divider.left { left: 70px; width: 184px; }
  .divider.right { left: 332px; width: 184px; }
  .divider-mark { position: absolute; left: 271px; top: 605px; }

  .author { position: absolute; left: 0; width: 586px; top: 648px; text-align: center; font-family: "Bebas Neue", sans-serif; font-weight: 400; font-size: 40px; letter-spacing: 0.3px; }
  .creds { position: absolute; left: 0; width: 586px; top: 693px; text-align: center; font-family: "Oswald", sans-serif; font-weight: 300; font-size: 12px; letter-spacing: 0.3px; text-transform: uppercase; }
  .creds i { display: inline-block; width: 4px; height: 4px; background: var(--white); border-radius: 50%; vertical-align: middle; margin: 0 4px; }
</style>
</head>
<body>
<div class="cover">

  <section class="back">
    <p class="tagline"><span class="rule"></span>The smart buyer’s guide to finding<span class="rule"></span><br>The right <em>boat</em> and boating with confidence</p>
    <h1 class="back-title">Think Twice <span class="gold">Buy</span></h1>
    <div class="blurb">
      <h2>Think Twice Buy:</h2>
      <p class="narrow">Before you spend thousands on a boat… spend a few hours learning what experienced boaters wish they knew.</p>
      <p class="narrow">Buying a recreational boat is exciting—but it can also be expensive, confusing, and full of costly mistakes.</p>
      <p class="justify">This practical guide helps first-time buyers understand how to evaluate boats, compare ownership options, recognize hidden costs, and avoid expensive surprises before signing the paperwork. Through easy-to-follow explanations, checklists, comparison tables, and illustrations, you'll gain the confidence to make informed decisions and purchase a boat that truly fits your lifestyle.</p>
      <p>Whether you're shopping for your first boat or upgrading to your next one, this book will help you buy smarter and avoid the mistakes that many owners only discover after it's too late.</p>
      <h2>You'll Learn How To:</h2>
      <ul class="learn-list">
        <li>Choose the right boat</li>
        <li>Compare ownership options</li>
        <li>Inspect boats with confidence</li>
        <li>Understand engines and systems</li>
        <li>Estimate ownership costs</li>
        <li>Avoid common buying mistakes</li>
        <li>Know when to hire a surveyor</li>
        <li>Negotiate from an informed position</li>
      </ul>
      <h2>About the Author</h2>
      <p>Captain Dorian L. Vask is a U.S. Coast Guard Licensed Captain, certified boating instructor, military veteran, and experienced recreational boater. Having trained thousands of students and delivered hundreds of vessels, he created the Think Twice… series to help new boaters avoid costly mistakes and enjoy safer, more rewarding time on the water.</p>
      <h2>Series Tagline</h2>
      <p class="tag-line">The Think Twice… Series</p>
      <p>Helping new recreational boaters make smarter decisions before buying, boating, and traveling.</p>
    </div>
  </section>

  <section class="spine">
    <p class="spine-text spine-title">Think Twice <span class="gold">Buy</span></p>
    <p class="spine-text spine-author">By Captain Dorian L. Vask</p>
    <p class="spine-text spine-creds">USCG Licensed Captain • Certified Boating Instructor • Veteran</p>
  </section>
  <svg class="spine-mark" width="20" height="20" viewBox="0 0 20 20" aria-hidden="true"><circle cx="10" cy="10" r="7" fill="none" stroke="#d18b12" stroke-width="1.6"/></svg>

  <section class="front">
    <div class="scene" role="img" aria-label="Photo of a motor boat cruising at sunset beneath a cable-stayed bridge over calm water"></div>
    <p class="tagline"><span class="rule"></span>The smart buyer’s guide to finding<span class="rule"></span><br>The right <em>boat</em> and boating with confidence</p>
    <h1 class="front-title line1">Think Twice</h1>
    <p class="front-title line2">Buy</p>

    <svg class="intro-mark" width="72" height="24" viewBox="0 0 72 24" aria-hidden="true">
      <line x1="0" y1="22" x2="16" y2="22" stroke="#d18b12" stroke-width="1.5"/>
      <line x1="56" y1="22" x2="72" y2="22" stroke="#d18b12" stroke-width="1.5"/>
      <circle cx="36" cy="14" r="6" fill="#021436"/>
    </svg>
    <p class="intro">A complete guide for<br><span class="gold">first time boat buyers</span><br>from shopping to sea<br>trial and beyond</p>

    <div class="badge">
      <svg class="badge-mark" width="24" height="24" viewBox="0 0 24 24" aria-hidden="true"><circle cx="12" cy="12" r="10" fill="none" stroke="#d18b12" stroke-width="2"/></svg>
      Avoid costly<br>mistakes<br>buy with<br><span class="gold">confidence</span>
      <span class="badge-rule"></span>
    </div>

    <ul class="features">
      <li class="feature" style="top:0">
        <div class="icon"><svg width="18" height="18" viewBox="0 0 18 18" aria-hidden="true"><circle cx="7" cy="7" r="5" fill="none" stroke="#fff" stroke-width="1.8"/><line x1="10.5" y1="10.5" x2="16" y2="16" stroke="#fff" stroke-width="2.2" stroke-linecap="round"/></svg></div>
        <span>Find the right boat<br>for your needs<br>and budget</span>
      </li>
      <li class="feature" style="top:40px">
        <div class="icon"><svg width="20" height="20" viewBox="0 0 20 20" aria-hidden="true"><circle cx="10" cy="10" r="8" fill="none" stroke="#fff" stroke-width="1.5"/><path d="M6 10.5l3 3 6-7" fill="none" stroke="#fff" stroke-width="1.8"/></svg></div>
        <span>Shop smart<br>and avoid<br>red flags</span>
      </li>
      <li class="feature" style="top:87px">
        <div class="icon"><svg width="18" height="18" viewBox="0 0 18 18" aria-hidden="true"><path d="M9 2v11H3z" fill="#fff"/><path d="M10 4v9h5z" fill="#fff"/><path d="M2 14h14l-2 2H4z" fill="#fff"/></svg></div>
        <span>Sea trial<br>like a pro</span>
      </li>
      <li class="feature" style="top:130px">
        <div class="icon"><svg width="16" height="18" viewBox="0 0 16 18" aria-hidden="true"><rect x="2" y="3" width="12" height="14" rx="1.5" fill="none" stroke="#fff" stroke-width="1.4"/><rect x="5" y="1" width="6" height="3" fill="#fff"/><line x1="5" y1="9" x2="11" y2="9" stroke="#fff"/><line x1="5" y1="12" x2="11" y2="12" stroke="#fff"/></svg></div>
        <span>Inspections,<br>survey &amp;<br>negotiations</span>
      </li>
      <li class="feature" style="top:177px">
        <div class="icon"><svg width="16" height="20" viewBox="0 0 16 20" aria-hidden="true"><text x="8" y="16" text-anchor="middle" font-family="Montserrat, sans-serif" font-weight="700" font-size="17" fill="#fff">$</text></svg></div>
        <span>Understand true<br>ownership cost</span>
      </li>
    </ul>

    <div class="divider left"></div>
    <div class="divider right"></div>
    <svg class="divider-mark" width="46" height="36" viewBox="0 0 46 36" aria-hidden="true"><circle cx="23" cy="18" r="14" fill="none" stroke="#d18b12" stroke-width="3"/></svg>

    <p class="author">By Captain Dorian L. Vask</p>
    <p class="creds">USCG-Licensed Captain<i></i>Certified Boating Instructor<i></i>Veteran</p>
  </section>

</div>
</body>
</html>
```